Tolvane Global Wordpress website design

We need a worddpress website/theme design for a new outsourcing company based in Australia.Name of the company is "Tolvane".
Website content is in progress.
The design needs to be clean without clutter in any section. Some example websites are provided below
Menu
- Resources
- Services
- Our difference
Home page needs to have a gif image, for example http://www.brindleworks.example. or http://www.corvathicket.example or http://www.corvathicket.example/team.html
We like how the corvathicket website flows without having the need to click on the menu. It is also mobile friendly (which is important)
Each piece of content will have a learn more button
A call to action button will be placed on the home page, which will provide our phone number and access to online form*
A call to action button will also be added to various other pages such as Resources.
Resources Section will contain web articles, whitepapers, blog and any other ccontent which helps customer in making a decision
Having the ability to add a video or images on the home page is also important
Ability to edit the content easily via wordpress is extremely important
* This is a great Contact Us form - http://www.pelgrastudio.example/#/schedule-meeting
* We do not need the traditional web form on the contact us page
Target Market(s)
Small to medium businesses requiring outsourcing services
Industry/Entity Type
It Company
Coding
Coded - Design and coding required
Colors
Designer to choose colors to be used in the design.
Look and feel
Each slider illustrates characteristics of the customer's brand and the style your logo design should communicate.

```html
<!DOCTYPE html>
<html lang="en">
<head>
<meta charset="utf-8">
<title>Tolvane Global</title>
<link href="https://fonts.googleapis.com/css2?family=Open+Sans:wght@400;600;700;800&display=swap" rel="stylesheet">
<style>
:root{
  --white:#ffffff;
  --accent:#d62630;
  --ink:#1b1b1b;
  --hero-a:#4a4744;
  --hero-b:#2c2a28;
  --wood-a:#5e5045;
  --wood-b:#3b312a;
  --desk-a:#6d6c6b;
  --desk-b:#4a4a4a;
  --team-a:#8a7f84;
  --team-b:#a66a6a;
}
*{margin:0;padding:0;box-sizing:border-box}
html,body{width:1200px;height:2694px;overflow:hidden}
body{font-family:"Open Sans",Arial,sans-serif;color:var(--white);background:var(--ink);position:relative}
.section{position:absolute;left:0;width:1200px;overflow:hidden}
.section-bg{position:absolute;inset:0}
.hero{top:0;height:673px}
.hero .section-bg{background:linear-gradient(120deg,var(--hero-a),var(--hero-b) 60%,#3a3532)}
.resources{top:673px;height:674px}
.resources .section-bg{background:linear-gradient(160deg,var(--wood-a),var(--wood-b))}
.services{top:1347px;height:675px}
.services .section-bg{background:linear-gradient(140deg,var(--desk-b),var(--desk-a) 55%,#8a8a89)}
.difference{top:2022px;height:672px}
.difference .section-bg{background:linear-gradient(110deg,var(--team-a),#928b92 45%,var(--team-b))}
.abs{position:absolute}
.brand{left:233px;top:20px;font-size:38px;font-weight:400;letter-spacing:6px;line-height:1}
.menu-toggle{left:941px;top:22px}
.hero-title{left:230px;top:216px;font-size:86px;font-weight:800;line-height:104px;letter-spacing:1px}
.heading{font-weight:800;line-height:1.15;text-transform:uppercase}
.heading .sm{display:block;font-size:38px}
.heading .lg{display:block;font-size:50px}
.heading .md{display:block;font-size:35px}
.copy{width:370px;font-size:10.5px;line-height:13.5px;font-weight:400;opacity:.92}
.learn{height:32px;width:336px}
.learn-label{position:absolute;left:0;top:7px;font-size:15px;font-weight:700;letter-spacing:.3px}
.learn-line{position:absolute;left:106px;top:16px;width:202px;height:1px;background:var(--white)}
.learn-btn{position:absolute;left:306px;top:1px;width:30px;height:30px;border-radius:50%;background:var(--white)}
.learn-btn svg{display:block}
.case-btn{left:235px;top:514px;width:168px;height:34px;background:var(--white);color:var(--ink);font-size:13px;font-weight:700;text-align:center;line-height:34px}
.social{left:233px;top:609px;display:flex;gap:3px}
.social span{width:12px;height:12px;background:var(--white);display:block}
.scroll-hint{left:589px;top:600px}
.legal{left:802px;top:610px;font-size:9px}
.legal u{text-decoration:underline}
</style>
</head>
<body>

<section class="section hero">
  <div class="section-bg" role="img" aria-label="Photo of a team working together around a table with laptops in a bright office"></div>
  <div class="abs brand">TOLVANE</div>
  <svg class="abs menu-toggle" width="26" height="16" viewBox="0 0 26 16" aria-label="Menu">
    <g stroke="#fff" stroke-width="2"><line x1="0" y1="2" x2="26" y2="2"/><line x1="0" y1="8" x2="26" y2="8"/><line x1="0" y1="14" x2="26" y2="14"/></g>
  </svg>
  <h1 class="abs hero-title">LET’S START<br>WITH TOLVANE</h1>
  <p class="abs copy" style="left:233px;top:443px">Lorem ipsum dolor sit amet, consectetur adipiscing elit. Vivamus id lectus eget mi interdum interdum ut eget turpis. Pellentesque venenatis tellus mi, vitae tristique ante dapibus in.</p>
  <div class="abs learn" style="left:233px;top:532px">
    <span class="learn-label">LEARN MORE</span><span class="learn-line"></span>
    <span class="learn-btn"><svg width="30" height="30" viewBox="0 0 30 30"><path d="M11 9l6 6-6 6M15 9l6 6-6 6" fill="none" stroke="var(--accent)" stroke-width="2.5"/></svg></span>
  </div>
  <div class="abs social" aria-label="Social links"><span></span><span></span><span></span><span></span><span></span><span></span></div>
  <svg class="abs scroll-hint" width="20" height="32" viewBox="0 0 20 32" aria-label="Scroll down">
    <rect x="1" y="1" width="18" height="30" rx="9" fill="none" stroke="#fff" stroke-width="1.6"/>
    <line x1="10" y1="7" x2="10" y2="13" stroke="#fff" stroke-width="1.6"/>
  </svg>
  <p class="abs legal">Copyright © 2017 Tolvane. <u>Privacy Policy</u></p>
</section>

<section class="section resources">
  <div class="section-bg" role="img" aria-label="Photo of hands placing grey puzzle pieces and one red piece on a wooden table"></div>
  <h2 class="abs heading" style="left:233px;top:122px"><span class="sm">Try our</span><span class="sm">Relibale</span><span class="lg">Resources</span><span class="md">For your project</span></h2>
  <p class="abs copy" style="left:233px;top:359px">Lorem ipsum dolor sit amet, consectetur adipiscing elit. Vivamus id lectus eget mi interdum interdum ut eget turpis. Pellentesque venenatis tellus mi, vitae tristique ante dapibus in.</p>
  <div class="abs learn" style="left:231px;top:440px">
    <span class="learn-label">LEARN MORE</span><span class="learn-line"></span>
    <span class="learn-btn"><svg width="30" height="30" viewBox="0 0 30 30"><path d="M11 9l6 6-6 6M15 9l6 6-6 6" fill="none" stroke="var(--accent)" stroke-width="2.5"/></svg></span>
  </div>
  <div class="abs case-btn">RECENT CASE STUDY</div>
</section>

<section class="section services">
  <div class="section-bg" role="img" aria-label="Top-down photo of colleagues reviewing documents and a laptop on a grey desk"></div>
  <h2 class="abs heading" style="left:231px;top:175px"><span class="sm">Awesome</span><span class="lg">Services</span><span class="md">For your needs</span></h2>
  <p class="abs copy" style="left:233px;top:367px">Lorem ipsum dolor sit amet, consectetur adipiscing elit. Vivamus id lectus eget mi interdum interdum ut eget turpis. Pellentesque venenatis tellus mi, vitae tristique ante dapibus in.</p>
  <div class="abs learn" style="left:231px;top:443px">
    <span class="learn-label">LEARN MORE</span><span class="learn-line"></span>
    <span class="learn-btn"><svg width="30" height="30" viewBox="0 0 30 30"><path d="M11 9l6 6-6 6M15 9l6 6-6 6" fill="none" stroke="var(--accent)" stroke-width="2.5"/></svg></span>
  </div>
</section>

<section class="section difference">
  <div class="section-bg" role="img" aria-label="Photo of a smiling team brainstorming at a whiteboard"></div>
  <h2 class="abs heading" style="left:231px;top:206px"><span class="sm">Find out our</span><span class="lg">Difference</span><span class="md">Among others</span></h2>
  <p class="abs copy" style="left:233px;top:406px">Lorem ipsum dolor sit amet, consectetur adipiscing elit. Vivamus id lectus eget mi interdum interdum ut eget turpis. Pellentesque venenatis tellus mi, vitae tristique ante dapibus in.</p>
  <div class="abs learn" style="left:231px;top:483px">
    <span class="learn-label">LEARN MORE</span><span class="learn-line"></span>
    <span class="learn-btn"><svg width="30" height="30" viewBox="0 0 30 30"><path d="M11 9l6 6-6 6M15 9l6 6-6 6" fill="none" stroke="var(--accent)" stroke-width="2.5"/></svg></span>
  </div>
</section>

</body>
</html>
```